Lanternleaf take out menu

We need a take out menu design using our menu attached. Info to include would be our address: 7816 Brindlewood Hollow Pkwy #204, Lafayette, LA 70508. Phone number is 337-514-2960. website is www.lanternleafgrv.com.

Industry/Entity Type

Asian Restaurant

```html
<!DOCTYPE html>
<html lang="en">
<head>
<meta charset="utf-8">
<title>Lanternleaf Take Out Menu</title>
<link rel="stylesheet" href="https://fonts.googleapis.com/css2?family=Crimson+Pro:wght@400;600;700&family=Libre+Baskerville:wght@400&display=swap">
<style>
:root{
  --ink:#1b1b1b;
  --muted:#4a4a4a;
  --red:#d3252b;
  --frame:#f0b7b4;
  --rule:#9a9a9a;
  --paper:#ffffff;
}
*{box-sizing:border-box;margin:0;padding:0}
html,body{width:1200px;height:737px;overflow:hidden;background:var(--paper)}
body{position:relative;font-family:"Crimson Pro",Georgia,serif;color:var(--ink)}
.panel{position:absolute;top:46px;width:268px;height:654px;border:1px solid var(--frame);background:var(--paper)}
.p1{left:30px}.p2{left:318px}.p3{left:612px}.p4{left:901px}
.brand{position:absolute;top:-22px;left:50%;transform:translateX(-50%);display:flex;align-items:center;gap:6px;background:var(--paper);padding:0 6px}
.brand-dot{width:34px;height:34px;border-radius:50%;background:var(--red)}
.brand-name{font-weight:700;font-size:13px;color:var(--red)}
.heading{position:absolute;left:0;right:0;text-align:center;font-family:"Libre Baskerville",Georgia,serif;font-size:12.5px;font-weight:400;letter-spacing:.3px;text-transform:uppercase}
.band{position:absolute;left:14px;right:14px;height:8px;display:flex;align-items:center}
.band::before,.band::after{content:"";flex:1;border-top:1px dotted var(--rule)}
.band span{background:#111;color:#fff;font-size:5.5px;font-weight:700;letter-spacing:1px;padding:1px 22px;clip-path:polygon(6px 0,calc(100% - 6px) 0,100% 50%,calc(100% - 6px) 100%,6px 100%,0 50%)}
.list{position:absolute;left:16px;right:16px}
.item{min-height:var(--row);border-bottom:1px dotted var(--rule);padding:2px 0 3px}
.item:last-child{border-bottom:none}
.line{display:flex;justify-content:space-between;align-items:baseline}
.name{font-weight:600;font-size:11px}
.price{font-size:10.5px}
.desc{font-size:6px;line-height:1.2;color:var(--muted);margin-top:1px;padding-right:18px}
.chili{display:inline-block;width:3px;height:7px;margin-left:2px;background:var(--red);border-radius:2px 2px 3px 3px;transform:rotate(25deg);vertical-align:-1px}
.contact{position:absolute;top:704px;width:268px;text-align:center;font-size:7.5px;color:var(--muted);white-space:nowrap}
.c1{left:30px}.c2{left:318px}.c3{left:612px}.c4{left:901px}
</style>
</head>
<body>

<section class="panel p1">
  <div class="brand"><span class="brand-dot"></span><span class="brand-name">Lanternleaf</span></div>
  <h2 class="heading" style="top:38px">Appetizers</h2>
  <div class="list" style="top:69px;--row:29px">
    <div class="item"><div class="line"><span class="name">Edamame</span><span class="price">$4</span></div><p class="desc">Seasoned &amp; boiled soy bean</p></div>
    <div class="item"><div class="line"><span class="name">Scallion Pancakes</span><span class="price">$6</span></div><p class="desc">Traditional Chinese flatbread folded with oil and minced scallions and pan fried</p></div>
    <div class="item"><div class="line"><span class="name">Lanternleaf Lettuce Wraps</span><span class="price">$8</span></div><p class="desc">Seasoned ground chicken drizzled with our top secret homemade sauce served with lettuce wraps</p></div>
    <div class="item"><div class="line"><span class="name">Salt &amp; Pepper Calamari</span><span class="price">$9</span></div><p class="desc">Crispy Calamari with Green &amp; red peppers and onions</p></div>
    <div class="item"><div class="line"><span class="name">Buddha Bang Shrimp</span><span class="price">$9</span></div><p class="desc">Crispy fried shrimp tossed in our creamy spicy sauce</p></div>
    <div class="item"><div class="line"><span class="name">Drunken Chicken <i class="chili"></i></span><span class="price">$8</span></div><p class="desc">Chicken, Thai chili in a house made spicy sauce</p></div>
    <div class="item"><div class="line"><span class="name">Sichuan Spiced Beef <i class="chili"></i><i class="chili"></i></span><span class="price">$9</span></div><p class="desc">Beef Shank, beef tripe, cilantro, peanuts and celery</p></div>
    <div class="item"><div class="line"><span class="name">Beef Crispy Bottom Bao</span><span class="price">$10</span></div><p class="desc">Pan fried crispy bottom Bao, stuffed with beef, drizzled with scallion and sesame (Fresh made to order, takes at least 20 min to serve)</p></div>
    <div class="item"><div class="line"><span class="name">Shrimp &amp; Beef Crispy Bottom Bao</span><span class="price">$10</span></div><p class="desc">Pan fried crispy bottom Bao, stuffed with beef and shrimp, drizzled with scallion and sesame (Fresh made to order, takes at least 20 min to serve)</p></div>
    <div class="item"><div class="line"><span class="name">Crispy Mala Beef Jerky <i class="chili"></i><i class="chili"></i><i class="chili"></i></span><span class="price">$9</span></div><p class="desc">Dry fried shredded beef with various peppers in sesame and peppercorn oil</p></div>
    <div class="item"><div class="line"><span class="name">Fried Chicken Dumplings (6)</span><span class="price">$6</span></div><p class="desc">Chinese dumpling stuffed with Chicken, Shiitake mushrooms and bamboo shoots</p></div>
    <div class="item"><div class="line"><span class="name">Red Oil Dumplings (6) <i class="chili"></i></span><span class="price">$7</span></div><p class="desc">Pork filled dumplings in Sichuan red oil sauce drizzled with sesame</p></div>
    <div class="item"><div class="line"><span class="name">Pork Egg Rolls (2)</span><span class="price">$4</span></div><p class="desc">Hand rolled with julienned veggies with our sweet n' sour mustard sauce</p></div>
    <div class="item"><div class="line"><span class="name">Vegetarian Spring Rolls (3)</span><span class="price">$4</span></div><p class="desc">Traditional Asian Roll served with a sweet chili sauce</p></div>
    <div class="item"><div class="line"><span class="name">Garlic Cucumber Salad</span><span class="price">$7</span></div><p class="desc">Sliced cucumber with a garlic vinaigrette</p></div>
    <div class="item"><div class="line"><span class="name">Hot n' Sour Soup <i class="chili"></i></span><span class="price">$4</span></div><p class="desc">Tangy broth with bamboo shoots, wood ear fungus, tofu, egg and carrots</p></div>
    <div class="item"><div class="line"><span class="name">West Lake Soup</span><span class="price">$4</span></div><p class="desc">Light creamy soup with ground beef, diced Shiitake mushroom, tofu, bamboo shoots, egg white and cilantro</p></div>
  </div>
</section>

<section class="panel p2">
  <div class="brand"><span class="brand-dot"></span><span class="brand-name">Lanternleaf</span></div>
  <h2 class="heading" style="top:38px">Noodles &amp; Rice</h2>
  <div class="list" style="top:69px;--row:33.6px">
    <div class="item"><div class="line"><span class="name">Lanternleaf Fried Rice</span><span class="price">$13</span></div><p class="desc">Shrimp, chicken, and beef, farm fresh eggs, onions, and scallions</p></div>
    <div class="item"><div class="line"><span class="name">Vegetarian White Fried Rice</span><span class="price">$13</span></div><p class="desc">Mixed vegetables with white rice</p></div>
    <div class="item"><div class="line"><span class="name">Lanternleaf Lo Mein</span><span class="price">$15</span></div><p class="desc">Shrimp, chicken, and beef, farm fresh eggs, onions, and scallions</p></div>
    <div class="item"><div class="line"><span class="name">Vegetarian Lo Mein</span><span class="price">$14</span></div><p class="desc">Mixed vegetables with lo mein noodles</p></div>
  </div>
  <h2 class="heading" style="top:218px">Vegetarian Dishes</h2>
  <div class="list" style="top:250px;--row:33.6px">
    <div class="item"><div class="line"><span class="name">Wok Tossed String Beans <i class="chili"></i></span><span class="price">$9</span></div><p class="desc">Fresh string beans mixed with pickled vegetables</p></div>
    <div class="item"><div class="line"><span class="name">Mapo Tofu <i class="chili"></i><i class="chili"></i></span><span class="price">$11</span></div><p class="desc">Soft Tofu, scallion, Sichuan peppercorn and peppers</p></div>
    <div class="item"><div class="line"><span class="name">Spicy Garlic Eggplant <i class="chili"></i></span><span class="price">$12</span></div><p class="desc">Chinese eggplant in spicy garlic sauce drizzled with scallions</p></div>
    <div class="item"><div class="line"><span class="name">Buddha's Delight</span><span class="price">$10</span></div><p class="desc">Seasonal vegetables wok tossed in our light soy garlic sauce</p></div>
    <div class="item"><div class="line"><span class="name">Stir-fried Eggplant Beans <i class="chili"></i></span><span class="price">$12</span></div><p class="desc">Chinese eggplant with sautéed green beans</p></div>
    <div class="item"><div class="line"><span class="name">Shiitake Baby Bok-Choy</span><span class="price">$12</span></div><p class="desc">Sautéed baby bok-choy with Shiitake mushrooms in brown sauce</p></div>
  </div>
  <h2 class="heading" style="top:475px">Kids Menu</h2>
  <div class="list" style="top:504px;--row:34px">
    <div class="item"><div class="line"><span class="name">Beef Lo Mein</span><span class="price">$5</span></div><p class="desc">Lo Mein noodles mixed with beef in garlic sauce</p></div>
    <div class="item"><div class="line"><span class="name">Chicken Fried Rice</span><span class="price">$5</span></div><p class="desc">Fried rice, farm fresh eggs, onions, and scallions</p></div>
    <div class="item"><div class="line"><span class="name">Sweet &amp; Sour Chicken</span><span class="price">$6</span></div><p class="desc">Bite sized crispy chicken with sweet &amp; sour sauce</p></div>
    <div class="item"><div class="line"><span class="name">Lemon Chicken</span><span class="price">$6</span></div><p class="desc">Bite sized crispy chicken in a sweet lemon sauce</p></div>
  </div>
</section>

<section class="panel p3">
  <div class="brand"><span class="brand-dot"></span><span class="brand-name">Lanternleaf</span></div>
  <h2 class="heading" style="top:38px">Entrees</h2>
  <div class="band" style="top:78px"><span>CHICKEN</span></div>
  <div class="list" style="top:112px;--row:37px">
    <div class="item"><div class="line"><span class="name">Kung Pao Chicken <i class="chili"></i></span><span class="price">$13</span></div><p class="desc">Chicken sautéed with roasted peanuts and scallions, dry red chili and whole Sichuan peppercorns in Kung Pao sauce</p></div>
    <div class="item"><div class="line"><span class="name">Orange Chicken</span><span class="price">$13</span></div><p class="desc">Battered-fried chicken breast with fried chili peppers and stir fried in a tangy orange flavored sauce</p></div>
    <div class="item"><div class="line"><span class="name">Double Pepper Chicken <i class="chili"></i><i class="chili"></i><i class="chili"></i></span><span class="price">$15</span></div><p class="desc">Farm raised chicken cube with fresh green peppercorns, Thai chili, Serrano pepper, and jalapenos</p></div>
    <div class="item"><div class="line"><span class="name">Crispy Spicy Chicken <i class="chili"></i><i class="chili"></i></span><span class="price">$14</span></div><p class="desc">Crispy diced chicken with Sichuan peppers, cilantro and sesame</p></div>
    <div class="item"><div class="line"><span class="name">General Tso's Chicken <i class="chili"></i></span><span class="price">$13</span></div><p class="desc">Battered-fried chicken breast, stir-fried in a sweet &amp; tangy chili sauce, scallions and chili pepper</p></div>
    <div class="item"><div class="line"><span class="name">Shredded Chicken in Spicy Garlic Sauce <i class="chili"></i></span><span class="price">$14</span></div><p class="desc">Tender shredded chicken, wood ear fungus, bamboo shoots in a classic spicy garlic sauce</p></div>
    <div class="item"><div class="line"><span class="name">Sweet &amp; Sour Chicken</span><span class="price">$13</span></div><p class="desc">Crispy Chicken glazed in a homemade sweet &amp; sour marinade</p></div>
  </div>
  <div class="band" style="top:399px"><span>SEAFOOD</span></div>
  <div class="list" style="top:432px;--row:34px">
    <div class="item"><div class="line"><span class="name">Kung Pao Shrimp <i class="chili"></i></span><span class="price">$16</span></div><p class="desc">Sautéed shrimp with roasted peanuts and scallions, dry red chili and whole Sichuan peppercorns in Kung Pao sauce</p></div>
    <div class="item"><div class="line"><span class="name">Rice Wine Shrimp &amp; Tofu <i class="chili"></i></span><span class="price">$18</span></div><p class="desc">Shrimp and Tofu braised in garlic pickled pepper sauce with rice wine</p></div>
    <div class="item"><div class="line"><span class="name">Shrimp in Spicy Garlic Sauce <i class="chili"></i></span><span class="price">$15</span></div><p class="desc">Shrimp with jicama ginger, garlic and scallions in a spicy garlic sauce</p></div>
    <div class="item"><div class="line"><span class="name">Lemon Peel Shrimp</span><span class="price">$15</span></div><p class="desc">Shrimp with fresh lemons in a sweet lemon sauce with vegetables</p></div>
    <div class="item"><div class="line"><span class="name">Rice Wine Fish <i class="chili"></i></span><span class="price">$14</span></div><p class="desc">White fish filet braised in pickled pepper sauce with rice wine</p></div>
  </div>
</section>

<section class="panel p4">
  <div class="brand"><span class="brand-dot"></span><span class="brand-name">Lanternleaf</span></div>
  <h2 class="heading" style="top:38px">Entrees</h2>
  <div class="band" style="top:78px"><span>CHEF SPECIALTIES</span></div>
  <div class="list" style="top:112px;--row:34px">
    <div class="item"><div class="line"><span class="name">Jasmine Tea Smoked Duck</span><span class="price">$24</span></div><p class="desc">Boneless half duck served with thinly sliced cucumber, scallions, house made duck sauce and soft flour wrap</p></div>
    <div class="item"><div class="line"><span class="name">Sizzling Cumin' Lamb <i class="chili"></i></span><span class="price">$16</span></div><p class="desc">Tender pieces of lamb rubbed in cumin, Sichuan peppers, celery and cilantro</p></div>
    <div class="item"><div class="line"><span class="name">Chef Lin's Spicy Beef <i class="chili"></i><i class="chili"></i></span><span class="price">$16</span></div><p class="desc">Angus beef in house made green peppercorn sauce, drizzled with fresh Sichuan peppercorns, Thai chili and cilantro</p></div>
    <div class="item"><div class="line"><span class="name">Chef Lin's Spicy Fish <i class="chili"></i><i class="chili"></i></span><span class="price">$17</span></div><p class="desc">Fish filet in house made green peppercorn sauce, drizzled with fresh Sichuan peppercorns, Thai chili and cilantro</p></div>
    <div class="item"><div class="line"><span class="name">General Tso's Scallops <i class="chili"></i></span><span class="price">$18</span></div><p class="desc">The perfect combination of tender scallops marinated in a sweet chili sauce with broccoli and red peppers</p></div>
  </div>
  <div class="band" style="top:336px"><span>BEEF &amp; PORK</span></div>
  <div class="list" style="top:368px;--row:33.6px">
    <div class="item"><div class="line"><span class="name">Dancing Beef <i class="chili"></i></span><span class="price">$14</span></div><p class="desc">Angus Beef slices on a bed of sizzling rice crackers, black peppercorn and Thai chili</p></div>
    <div class="item"><div class="line"><span class="name">Oyster Beef</span><span class="price">$14</span></div><p class="desc">Tender cuts of steak wok fried and marinated in a homemade oyster sauce</p></div>
    <div class="item"><div class="line"><span class="name">Double Pepper Beef <i class="chili"></i><i class="chili"></i><i class="chili"></i></span><span class="price">$16</span></div><p class="desc">Angus flank cubes with fresh green peppercorns, Thai chili, Serrano pepper and celery</p></div>
    <div class="item"><div class="line"><span class="name">Black Pepper Steak <i class="chili"></i></span><span class="price">$15</span></div><p class="desc">Tender cuts of steak mixed with onions and red and green bell peppers</p></div>
    <div class="item"><div class="line"><span class="name">Singapore Baby Back Ribs</span><span class="price">$16</span></div><p class="desc">Baby back ribs rubbed in a Thai inspired sweet tangy glaze</p></div>
    <div class="item"><div class="line"><span class="name">Dancing Pork Belly</span><span class="price">$15</span></div><p class="desc">Braised Pork Belly sitting on rice cracker</p></div>
    <div class="item"><div class="line"><span class="name">Twice Cooked Pork <i class="chili"></i></span><span class="price">$14</span></div><p class="desc">Stir fried Pork Belly slices with leek and fermented black beans</p></div>
  </div>
</section>

<p class="contact c1">7816 Brindlewood Hollow Pkwy #204, Lafayette, LA 70508</p>
<p class="contact c2">337-514-2960</p>
<p class="contact c3">www.lanternleafgrv.com</p>
<p class="contact c4">337-514-2960 · www.lanternleafgrv.com</p>

</body>
</html>
```